K7R Business Cards

Business Cards

Contact Information for Business Card

Company name, owner name, license #s, phone & email

Requirements
Should not have
• mailing address

```html
<!DOCTYPE html>
<html lang="en">
<head>
<meta charset="utf-8">
<title>K7R Realty Business Cards</title>
<link href="https://fonts.googleapis.com/css2?family=Montserrat:wght@700&family=Roboto:wght@400;500&display=swap" rel="stylesheet">
<style>
  :root {
    --brand-blue: #1c3a8a;
    --brand-red: #c4161c;
    --ink: #222222;
    --paper: #ffffff;
    --stage: #c9c9c9;
    --watermark: #efefef;
  }
  * { box-sizing: border-box; margin: 0; padding: 0; }
  html, body { width: 1200px; height: 802px; overflow: hidden; }
  body {
    background: var(--stage);
    display: flex;
    align-items: center;
    justify-content: center;
    gap: 60px;
    font-family: "Roboto", Arial, sans-serif;
  }
  .card {
    position: relative;
    width: 530px;
    height: 303px;
    border-radius: 18px;
    overflow: hidden;
    border-bottom: 4px solid var(--brand-red);
    box-shadow: 0 10px 24px rgba(0,0,0,0.25);
  }
  .card--front { background: var(--paper); }
  .card--back {
    background: var(--brand-blue);
    display: flex;
    align-items: center;
    justify-content: center;
  }
  .watermark {
    position: absolute;
    left: 160px;
    top: 10px;
    font-family: "Montserrat", Arial, sans-serif;
    font-weight: 700;
    font-size: 56px;
    line-height: 1;
    color: var(--watermark);
    letter-spacing: 2px;
  }
  .portrait {
    position: absolute;
    right: 0;
    top: 0;
    width: 240px;
    height: 303px;
    background: linear-gradient(180deg, #ffffff 0%, #f1f1f1 40%, #3a3a3a 72%, #1e1e1e 100%);
  }
  .brand-name {
    font-family: "Montserrat", Arial, sans-serif;
    font-weight: 700;
    color: var(--brand-blue);
  }
  .card--front .brand-name {
    position: absolute;
    left: 34px;
    top: 70px;
    font-size: 32px;
    line-height: 1;
  }
  .card--back .brand-name {
    color: var(--paper);
    font-size: 64px;
  }
  .name-band {
    position: absolute;
    left: 0;
    top: 128px;
    width: 290px;
    height: 42px;
    background: var(--brand-blue);
    clip-path: polygon(0 0, 100% 0, 88% 100%, 0 100%);
    border-top: 4px solid var(--brand-red);
    display: flex;
    align-items: center;
    padding-left: 34px;
  }
  .name-band__text {
    font-family: "Montserrat", Arial, sans-serif;
    font-weight: 700;
    font-size: 21px;
    color: var(--paper);
    letter-spacing: 0.5px;
  }
  .contact {
    position: absolute;
    left: 34px;
    top: 184px;
    width: 250px;
    color: var(--ink);
  }
  .contact__licenses { font-size: 12px; line-height: 16px; margin-bottom: 8px; }
  .contact__line {
    display: flex;
    align-items: center;
    gap: 8px;
    margin-bottom: 6px;
  }
  .contact__phone { font-size: 18px; font-weight: 500; }
  .contact__email { font-size: 13px; color: var(--brand-red); }
  .contact__icon { width: 16px; height: 16px; flex: none; }
</style>
</head>
<body>
  <section class="card card--front" aria-label="Business card front">
    <div class="watermark" aria-hidden="true">K7R</div>
    <div class="portrait" role="img" aria-label="Portrait photo of the agent in a dark suit and patterned tie"></div>
    <div class="brand-name">K7R Realty</div>
    <div class="name-band"><span class="name-band__text">Dana Merrick</span></div>
    <div class="contact">
      <p class="contact__licenses">License # MN 40512873<br>Broker License # MN 40099214</p>
      <p class="contact__line">
        <svg class="contact__icon" viewBox="0 0 16 16" aria-hidden="true">
          <circle cx="8" cy="8" r="8" fill="var(--brand-red)"/>
          <path d="M5.2 4.2l1.5-.3.8 1.9-1 .7a5 5 0 0 0 2.6 2.6l.7-1 1.9.8-.3 1.5c-3.3.4-6.6-2.9-6.2-6.2z" fill="#fff"/>
        </svg>
        <span class="contact__phone">555-201-4786</span>
      </p>
      <p class="contact__line">
        <svg class="contact__icon" viewBox="0 0 16 16" aria-hidden="true">
          <circle cx="8" cy="8" r="8" fill="var(--brand-red)"/>
          <rect x="4" y="5" width="8" height="6" rx="0.8" fill="#fff"/>
          <path d="M4.3 5.4L8 8.3l3.7-2.9" stroke="var(--brand-red)" stroke-width="0.9" fill="none"/>
        </svg>
        <span class="contact__email">dmerrick@mailbox.com</span>
      </p>
    </div>
  </section>

  <section class="card card--back" aria-label="Business card back">
    <div class="brand-name">K7R Realty</div>
  </section>
</body>
</html>
```